Commercial brochure presenting independent commercial activity

I would like to create a commercial brochure for my new professional activity.

This is a personal and not business oriented brochure because I will become an independent project assistant to assist engineering offices with one-off missions.

I want a 4 page A4 brochure

• Page 1: Logo, personal photo
• Page 2 and 3: Personal presentation and presentation of my activities
• Page4: contact information

My target audience: engineering offices and design offices

The objective of the brochure: it is to make my profile interesting so that design offices will want to use my services when there is demand

Sector of activity: food, chemical, pharmaceutical industry
The text of the brochure must remain in French and contain what is in the attached file

On page 1, you must keep a space for a photo of my profile which I will insert later because I do not have it yet and insert my monogram (it can be reworked to be inserted in the brochure)
The image with the logo (K/M) is the color range I want

engineering offices and design offices

industrie alimentaire, chimique, pharmaceutique

Sans Serif

0094D4
00A9DD
6FCCEA
C7EBF8
E9F6FB

• The plate must comply with current codes. Each reader must think that I am dynamic and that my services are of quality and equivalent to the presentation

```html
<!DOCTYPE html>
<html lang="fr">
<head>
<meta charset="utf-8">
<title>Julien Morel-Favre – Brochure</title>
<link href="https://fonts.googleapis.com/css2?family=Italiana&family=Poppins:wght@400;500;600;700&display=swap" rel="stylesheet">
<style>
:root{
  --backdrop:#cbcbcb;
  --ink-dark:#212121;
  --ink-text:#1c1c1c;
  --blue:#0094D4;
  --blue-bright:#00A9DD;
  --blue-soft:#6FCCEA;
  --blue-pale:#C7EBF8;
  --blue-mist:#E9F6FB;
  --navy:#0a4f9c;
  --white:#ffffff;
  --grey-ring:#3a3a3a;
}
*{box-sizing:border-box;margin:0;padding:0}
html,body{width:894px;height:1200px;overflow:hidden;background:var(--backdrop)}
body{position:relative;font-family:'Poppins',sans-serif;color:var(--ink-text)}
.display{font-family:'Italiana',serif;font-weight:400}
.page{position:absolute;width:352px;height:498px;overflow:hidden;box-shadow:0 6px 14px rgba(0,0,0,.28)}
.page--cover{left:78px;top:80px;background:var(--ink-dark)}
.page--expertise{left:463px;top:80px;background:var(--white)}
.page--advantage{left:78px;top:610px;background:var(--ink-dark)}
.page--contact{left:463px;top:610px;background:var(--ink-dark)}
.abs{position:absolute}
.photo{position:absolute;border-radius:50%}

/* Cover */
.cover-brand{left:0;width:155px;top:60px;text-align:center;color:var(--white)}
.brand-name{font-family:'Italiana',serif;font-size:10px;letter-spacing:.3px;white-space:nowrap}
.brand-tag{font-family:'Italiana',serif;font-size:4.6px;margin-top:2px;white-space:nowrap}
.brand-dot{width:9px;height:9px;border-radius:50%;border:1px solid var(--white);margin:0 auto 5px}
.cover-city{left:134px;top:-124px;width:270px;height:270px;background:linear-gradient(160deg,#17a7ec,#0a6fc4 60%,#0b5aa8)}
.cover-ring{left:-2px;top:112px;width:248px;height:248px;background:var(--ink-dark)}
.cover-portrait{left:25px;top:139px;width:194px;height:194px;border:1.5px solid var(--blue);padding:6px;background:var(--ink-dark)}
.cover-portrait .fill{width:100%;height:100%;border-radius:50%;background:radial-gradient(circle at 55% 45%,#f1f1f1,#cdd5dc 60%,#9aa6b1)}
.cover-title{left:27px;top:374px;color:var(--white)}
.cover-title .line1{font-family:'Italiana',serif;font-size:21px;line-height:1}
.cover-title .line2{font-family:'Italiana',serif;font-size:47px;line-height:1;color:var(--blue);margin-top:-1px}
.cover-dash{left:27px;top:445px;width:13px;height:1.5px;background:var(--blue)}
.cover-sub{left:27px;top:458px;font-size:9.6px;color:var(--white);font-weight:400;white-space:nowrap}

/* Expertise page */
.exp-top{left:0;top:0;width:352px;height:197px;background:var(--ink-dark)}
.exp-skyline{left:0;top:300px;width:352px;height:198px;background:linear-gradient(180deg,rgba(255,255,255,0),#e4e6e8 55%,#d4d7da)}
.exp-head{left:30px;top:27px;color:var(--white)}
.exp-head h1{font-size:15.5px;line-height:1.1;white-space:nowrap}
.exp-head h1 span{color:var(--blue)}
.exp-head h2{font-size:6.6px;font-weight:700;margin-top:2px}
.exp-intro{left:30px;top:70px;width:295px;font-size:5.3px;line-height:1.25;color:var(--white)}
.exp-box{left:30px;top:105px;width:141px;height:334px;background:linear-gradient(180deg,#0c96dc,#1aa2e8);padding:14px 12px 0 13px;color:var(--white)}
.exp-box h3{font-size:12.5px;margin-bottom:10px;white-space:nowrap}
.exp-group{margin-bottom:16px}
.exp-group--tight{margin-bottom:12px}
.exp-group h4{font-size:6.6px;font-weight:600;color:var(--ink-dark);margin-bottom:3px}
.ticks{list-style:none}
.ticks li{position:relative;padding-left:8px;font-size:5.3px;line-height:1.22;margin-bottom:2.8px}
.ticks li::before{content:"";position:absolute;left:0;top:1px;width:5px;height:5px;background:var(--white);border-radius:1px}
.ticks li::after{content:"";position:absolute;left:1.4px;top:1.6px;width:1.5px;height:2.6px;border:solid var(--blue);border-width:0 1px 1px 0;transform:rotate(45deg)}
.exp-circle{width:108px;height:108px;border:1.5px solid var(--blue);padding:4px;background:var(--white)}
.exp-circle .fill{width:100%;height:100%;border-radius:50%}
.footer{left:27px;top:456px;width:300px;height:20px}
.footer .fname{position:absolute;left:0;top:2px;font-family:'Italiana',serif;font-size:7.6px;color:var(--blue);white-space:nowrap}
.footer .ftag{position:absolute;left:0;top:12px;font-family:'Italiana',serif;font-size:3.6px;color:var(--blue);white-space:nowrap}
.footer .rule{position:absolute;left:90px;top:14px;width:200px;height:.6px;background:var(--blue)}
.footer .pg{position:absolute;left:291px;top:9px;width:19px;height:9px;background:var(--blue);color:var(--white);font-family:'Italiana',serif;font-size:5.5px;line-height:9px;text-align:center;clip-path:polygon(18% 0,100% 0,100% 100%,0 100%)}
.footer--dark .fname,.footer--dark .ftag{color:var(--white)}

/* Advantage page */
.adv-top{left:0;top:0;width:352px;height:207px;background:var(--white)}
.adv-title{left:29px;top:27px;font-size:15.5px;color:var(--ink-dark)}
.adv-title span{color:var(--blue)}
.adv-rule{left:67px;top:58px;width:.6px;height:130px;background:#d9d9d9}
.adv-item{left:77px;width:250px}
.adv-item h4{font-size:7px;font-weight:700;color:var(--navy);line-height:1.1}
.adv-item p{font-size:5.2px;line-height:1.22;margin-top:1px}
.adv-icon{left:30px;width:24px;height:24px}
.adv-box{left:189px;top:195px;width:141px;height:178px;background:linear-gradient(180deg,#0c96dc,#1aa2e8);padding:15px 14px 0 16px;color:var(--white)}
.adv-box h3{font-size:12.5px;margin-bottom:8px;white-space:nowrap}
.adv-box p{font-size:5.25px;line-height:1.45;font-weight:500}
.adv-cta{left:207px;top:315px;width:106px;height:119px;background:var(--white);padding:13px 8px 0 14px}
.adv-cta strong{display:block;font-size:9.4px;line-height:1.2;color:var(--blue);font-weight:700}
.adv-cta span{display:block;font-size:7.8px;line-height:1.22;color:var(--ink-dark)}
.adv-photo{left:27px;top:240px;width:136px;height:136px;border:1.5px solid var(--blue);padding:4px;background:var(--ink-dark)}
.adv-photo .fill{width:100%;height:100%;border-radius:50%;background:linear-gradient(160deg,#c9c3bd,#8b8580 55%,#5d5a58)}
.adv-stat{left:30px;top:408px;color:var(--white);display:flex;align-items:flex-start}
.adv-stat .num{font-family:'Italiana',serif;font-size:35px;line-height:1;color:var(--blue)}
.adv-stat .when{margin-left:7px;margin-top:1px;font-size:9.5px;line-height:.98}
.adv-stat .year{display:block;font-size:5.5px;color:var(--blue);letter-spacing:2px;margin-top:3px;font-weight:600}

/* Contact page */
.ct-ring{left:-64px;top:-53px;width:248px;height:248px;border:1px solid var(--grey-ring)}
.ct-photo{left:-54px;top:-43px;width:228px;height:228px;background:linear-gradient(150deg,#1aa6ea,#0d6fc2 55%,#094e99)}
.ct-brand{left:0;width:352px;top:316px;text-align:center;color:var(--white)}
.ct-list{left:0;width:352px;top:381px;text-align:center;color:var(--white);font-size:7.6px;line-height:1.2}
.ct-item{margin-bottom:7px}
.ct-icon{display:block;margin:0 auto 2px;width:11px;height:11px}
</style>
</head>
<body>

<!-- Page 1 : cover -->
<section class="page page--cover">
  <div class="photo cover-city" role="img" aria-label="Vue aérienne de gratte-ciel teintée en bleu"></div>
  <div class="photo cover-ring"></div>
  <div class="photo cover-portrait"><div class="fill" role="img" aria-label="Emplacement pour la photo de profil"></div></div>
  <div class="abs cover-brand">
    <div class="brand-dot"></div>
    <div class="brand-name">Julien Morel-Favre</div>
    <div class="brand-tag">Assistant de projet indépendant</div>
  </div>
  <div class="abs cover-title">
    <div class="line1">Julien Morel</div>
    <div class="line2">Favre</div>
  </div>
  <div class="abs cover-dash"></div>
  <p class="abs cover-sub">Un atout précieux pour votre bureau d'études</p>
</section>

<!-- Page 2 : expertise -->
<section class="page page--expertise">
  <div class="abs exp-top"></div>
  <div class="abs exp-skyline" role="img" aria-label="Silhouette de ville estompée en gris clair"></div>
  <div class="abs exp-head">
    <h1 class="display">Julien Morel-<span>Favre</span></h1>
    <h2>Un atout précieux pour votre bureau d'études</h2>
  </div>
  <p class="abs exp-intro">Avec plus de 30 ans d'expérience dans l'industrie, je suis un expert chevronné en conception, gestion de projets et sécurité. J'offre mes services d'assistant de projet indépendant pour vous aider à gérer les pics de charge et les besoins spécifiques de votre bureau d'études.</p>
  <div class="abs exp-box">
    <h3 class="display">Mon expertise</h3>
    <div class="exp-group">
      <h4>Conception &amp; Design</h4>
      <ul class="ticks">
        <li>Maquettes 3D (Tracéo Plant 3D)</li>
        <li>Plans, schémas, RI/P&amp;ID, Flowsheets</li>
        <li>Spécifications, catalogues, définition des fournitures</li>
      </ul>
    </div>
    <div class="exp-group">
      <h4>Gestion de Projets</h4>
      <ul class="ticks">
        <li>Rédaction d'appels d'offre</li>
        <li>Préparation de budgets</li>
        <li>Réalisation de plannings</li>
        <li>Estimations budgétaires</li>
        <li>Réponse aux appels d'offre</li>
      </ul>
    </div>
    <div class="exp-group">
      <h4>Sécurité</h4>
      <ul class="ticks">
        <li>Sécurité machine</li>
        <li>Plans de montage</li>
        <li>Edition de PHS</li>
      </ul>
    </div>
    <div class="exp-group exp-group--tight">
      <h4>Documentation Technique :</h4>
      <ul class="ticks">
        <li>DESP</li>
        <li>Documentations spécifiques</li>
      </ul>
    </div>
    <div class="exp-group">
      <h4>Expertise</h4>
      <ul class="ticks">
        <li>Ma connaissance approfondie de la métallurgie (tuyauterie, serrurerie, chaudronnerie, charpente métallique, montage) me permet de garantir des études complètes et d'éviter les oublis.</li>
      </ul>
    </div>
  </div>
  <div class="photo exp-circle" style="left:208px;top:106px"><div class="fill" role="img" aria-label="Photo de tours de bureaux en ville" style="background:linear-gradient(180deg,#8fa9c4,#5d6f86 60%,#3d4a58)"></div></div>
  <div class="photo exp-circle" style="left:208px;top:219px"><div class="fill" role="img" aria-label="Photo d'une équipe en réunion autour d'une table" style="background:linear-gradient(180deg,#c9c6c2,#9e8f80 60%,#c9a57c)"></div></div>
  <div class="photo exp-circle" style="left:208px;top:332px"><div class="fill" role="img" aria-label="Photo de deux hommes d'affaires se serrant la main" style="background:linear-gradient(160deg,#c7d0d8,#7d8a97 55%,#3b4250)"></div></div>
  <div class="abs footer">
    <div class="fname">Julien Morel-Favre</div>
    <div class="ftag">Assistant de projet indépendant</div>
    <div class="rule"></div>
    <div class="pg">Pg 1</div>
  </div>
</section>

<!-- Page 3 : advantage -->
<section class="page page--advantage">
  <div class="abs adv-top"></div>
  <h2 class="abs adv-title display">Votre <span>avantage</span></h2>
  <div class="abs adv-rule"></div>

  <svg class="abs adv-icon" style="top:58px" viewBox="0 0 24 24" fill="none" stroke="#0094D4" stroke-width="1.2" stroke-linecap="round"><circle cx="9" cy="9" r="5"/><path d="M6 21h12M9 14v7M15 14l5-5M13 19l7-7"/></svg>
  <svg class="abs adv-icon" style="top:93px" viewBox="0 0 24 24" fill="none" stroke="#0094D4" stroke-width="1.2" stroke-linecap="round"><circle cx="12" cy="12" r="4"/><circle cx="12" cy="12" r="7.5"/><path d="M3 4h6M3 4v5M21 20h-6M21 20v-5"/></svg>
  <svg class="abs adv-icon" style="top:130px" viewBox="0 0 24 24" fill="none" stroke="#0094D4" stroke-width="1.2" stroke-linecap="round"><circle cx="12" cy="12" r="9"/><path d="M12 6v6l4 3"/></svg>
  <svg class="abs adv-icon" style="top:161px" viewBox="0 0 24 24" fill="none" stroke="#0094D4" stroke-width="1.2" stroke-linecap="round"><circle cx="12" cy="6" r="3"/><path d="M3 15l5-3 4 3 4-3 5 3M6 18l4 3h4l4-3"/></svg>

  <div class="abs adv-item" style="top:62px"><h4>Connaissance des besoins des concepteurs et des fabricants</h4><p>J'ai travaillé des deux côtés, ce qui me permet de comprendre les défis et les attentes de chacun</p></div>
  <div class="abs adv-item" style="top:97px"><h4>Flexibilité</h4><p>Je suis disponible pour des missions ponctuelles et à durée déterminée, sans engagement à long terme.</p></div>
  <div class="abs adv-item" style="top:134px"><h4>Efficacité</h4><p>Je peux vous aider à gérer les surcharges de travail et à respecter vos délais.</p></div>
  <div class="abs adv-item" style="top:164px"><h4>Collaboration fluide</h4><p>Je suis à votre disposition pour discuter de vos besoins et vous proposer des solutions sur mesure</p></div>

  <div class="abs adv-box">
    <h3 class="display">Un atout unique</h3>
    <p>Malgré mon handicap en fauteuil roulant, je suis totalement opérationnel et mon expérience me permet de vous offrir une expertise de haut niveau. Je suis disponible à 35% dès septembre 2024 et je suis prêt à mettre mon expertise et mon dynamisme au service de votre succès</p>
  </div>
  <div class="abs adv-cta">
    <strong>N'hésitez pas<br>à me contacter<br>pour</strong>
    <span>discuter de vos besoins et découvrir comment je peux vous aider à atteindre vos objectifs</span>
  </div>
  <div class="photo adv-photo"><div class="fill" role="img" aria-label="Photo d'une équipe travaillant autour d'un ordinateur portable"></div></div>
  <div class="abs adv-stat">
    <span class="num">35%</span>
    <span class="when">DÈS<br>SEPTEMBRE<span class="year">2024</span></span>
  </div>
  <div class="abs footer footer--dark" style="left:27px">
    <div class="fname">Julien Morel-Favre</div>
    <div class="ftag">Assistant de projet indépendant</div>
    <div class="rule"></div>
    <div class="pg">Pg 2</div>
  </div>
</section>

<!-- Page 4 : contact -->
<section class="page page--contact">
  <div class="photo ct-ring"></div>
  <div class="photo ct-photo" role="img" aria-label="Photo d'une réunion d'équipe teintée en bleu"></div>
  <div class="abs ct-brand">
    <div class="brand-dot"></div>
    <div class="brand-name">Julien Morel-Favre</div>
    <div class="brand-tag">Assistant de projet indépendant</div>
  </div>
  <div class="abs ct-list">
    <div class="ct-item">
      <svg class="ct-icon" viewBox="0 0 12 12"><circle cx="6" cy="6" r="6" fill="#0094D4"/><path d="M6 9.3C4.6 7.6 4 6.6 4 5.4a2 2 0 0 1 4 0c0 1.2-.6 2.2-2 3.9z" fill="#fff"/><circle cx="6" cy="5.3" r=".7" fill="#0094D4"/></svg>
      Rue des Tilleuls 8<br>1870 Montval
    </div>
    <div class="ct-item">
      <svg class="ct-icon" viewBox="0 0 12 12"><circle cx="6" cy="6" r="6" fill="#0094D4"/><rect x="3.2" y="4" width="5.6" height="4" fill="none" stroke="#fff" stroke-width=".7"/><path d="M3.2 4L6 6.3 8.8 4" fill="none" stroke="#fff" stroke-width=".7"/></svg>
      julien@morel-favre.ch
    </div>
    <div class="ct-item">
      <svg class="ct-icon" viewBox="0 0 12 12"><circle cx="6" cy="6" r="6" fill="#0094D4"/><path d="M4.2 3.2l1 1.3-.6.8c.4.9 1.1 1.6 2 2l.8-.6 1.3 1-.6 1C6 8.7 3.3 6 3.2 4z" fill="#fff"/></svg>
      +41 79 000 12 34
    </div>
  </div>
</section>

</body>
</html>
```